Paper Lanterns Fading ---Marla Quindstrom; EP cover

I am a pop artist and need my name and title of the EP designed onto professional pictures.(Paper Lanterns Fading---Marla Quindstrom) I am open to color for lettering and other design elements. I'd really like something that compliments the photo(s)! To get a feel for what I'm looking for-- reference past CD covers from pop artists like- Tessaly Vornet, Dana Prewitt, Lira Moskin, etc. Can't wait to see what you design!

Font styles to use
Serif
Sans Serif
Decorative
Script

Requirements
Must have
• I would like very little alteration to the pictures other than fitting pictures to the dimensions required for the CD cover. Some softening or a little bit of blurring to the picture is ok.
Nice to have
• My initial thought was to keep everything grayscale to match the photos, but if you feel so inspired--create!
Should not have
• No flashy lettering

```html
<!DOCTYPE html>
<html lang="en">
<head>
<meta charset="utf-8">
<title>Marla Quindstrom – Paper Lanterns Fading</title>
<link rel="stylesheet" href="https://fonts.googleapis.com/css2?family=Cinzel:wght@700&display=swap">
<style>
  :root {
    --page-bg: #ebeceb;
    --title-lime: #cfdc3a;
    --photo-dark: #1c1c1c;
    --photo-mid: #6e6e6e;
    --photo-light: #bdbdbd;
    --band-blue: #4fb8e8;
    --band-blue-light: #8fd3f2;
    --band-lime: #c6d92e;
    --band-pink: #df6aa8;
    --band-orange: #f7b51b;
    --sliver-black: #111111;
  }
  * { margin: 0; padding: 0; box-sizing: border-box; }
  html, body {
    width: 1200px;
    height: 1000px;
    overflow: hidden;
    background: var(--page-bg);
  }
  .cover {
    position: absolute;
    left: 110px;
    top: 10px;
    width: 980px;
    height: 980px;
    overflow: hidden;
  }
  .cover-photo {
    position: absolute;
    inset: 0;
    background:
      radial-gradient(ellipse 38% 48% at 56% 42%, var(--photo-light) 0%, var(--photo-mid) 55%, transparent 80%),
      linear-gradient(90deg, var(--photo-dark) 0%, #3a3a3a 35%, #8a8a8a 75%, #9d9d9d 100%);
  }
  .cover-bands {
    position: absolute;
    inset: 0;
    width: 980px;
    height: 980px;
  }
  .cover-titles {
    position: absolute;
    left: 40px;
    top: 30px;
    color: var(--title-lime);
    font-family: "Cinzel", serif;
    font-weight: 700;
    text-transform: uppercase;
  }
  .artist-name {
    font-size: 37px;
    letter-spacing: 1px;
    line-height: 1;
  }
  .ep-title {
    margin-top: 20px;
    font-size: 25px;
    letter-spacing: 0.5px;
    line-height: 1;
  }
</style>
</head>
<body>
  <main class="cover">
    <div class="cover-photo" role="img" aria-label="Black and white portrait photograph of the artist with long wavy hair, looking down"></div>

    <svg class="cover-bands" viewBox="0 0 980 980" aria-hidden="true">
      <defs>
        <linearGradient id="blueBand" x1="0" y1="0" x2="1" y2="0.3">
          <stop offset="0" stop-color="var(--band-blue)"/>
          <stop offset="0.6" stop-color="var(--band-blue-light)"/>
          <stop offset="1" stop-color="var(--band-blue)"/>
        </linearGradient>
      </defs>
      <polygon points="0,363 0,372 505,893 510,888" fill="var(--band-blue)"/>
      <polygon points="0,388 0,396 470,880 474,876" fill="var(--band-blue)"/>
      <polygon points="0,440 550,980 0,980" fill="url(#blueBand)"/>
      <polygon points="120,560 300,735 296,740" fill="var(--sliver-black)"/>
      <polygon points="0,600 380,980 0,980" fill="var(--band-lime)"/>
      <polygon points="0,740 240,980 0,980" fill="var(--band-pink)"/>
      <polygon points="30,790 220,980 205,980 25,800" fill="var(--sliver-black)"/>
      <polygon points="0,800 150,980 0,980" fill="var(--band-orange)"/>
    </svg>

    <header class="cover-titles">
      <h1 class="artist-name">Marla Quindstrom</h1>
      <h2 class="ep-title">Paper Lanterns Fading</h2>
    </header>
  </main>
</body>
</html>
```